Walk Bold Stay Kind Ebook and Print book cover

I need a professional, eye catching cover that will stand out. The title of the book is "Walk Bold Stay Kind: 47 Quiet Rules For Calm and Wonder" It is a self-help personal transformation book by author Dale Ormsby. The cover will be on both print and ebook covers. I want something that is similar yet different to best-selling books in the genre, nothing too boring. A blue background might work, but it isn't a requirement. I'm open to other colors as long as it's powerful, professional, and screams "Buy me because this book is going to change your life!"
Updates

So far, 3 designs (3 of the 4 star rated designs) are in contention, but they all can be improved. I think the book cover should best convey "thinking smart" in a dynamic way. I'll run another poll in a day or so when I get additional designs I like. Added Thursday, May 4, 2017

Based on current designs, I wanted to provide additional guidance. The title and image should pop and be clearly visible at a distance as a thumbnail. Also, I'm wanting something bold and creative but not too confusing. I currently have a couple solid designs that are in contention to win, but I have another 7 days left for the project. I extended it to 10 days from the initial 5. I'll include several more polls for my followers and will likely pick the top ranking design based off the series of polls and will be eliminating lower ranking designs with each new poll and set of promising designs that come in. Finally, I may ask to see what the back will look like on the print version since I'll need both the Lumora and print (5" by 8") designs. Added Saturday, May 6, 2017

It's been recommended by some that I should have my own picture on the cover. I'm not completely convinced, but I would like to see some additional designs that incorporate my photo (touched up to remove the shine from my forehead and the label brand name removed from the t-shire) into a cover design. I have several good designs coming in, so typeset and professional looking font is extremely important. Blue is also preferred but not required. I've attached the photo on the brief for those who want to submit a design with that photo. Added Saturday, May 6, 2017

Target Market(s)

Working age adults seeking personal transformation and self improvement.

Industry/Entity Type

Motivation

Requirements
Must have
• Creativity. Eye catching. Striking. Contrast. Looks good close up and as a thumbnail at a distance. Font should be easy to read and pop from the cover along with the design.
Nice to have
• Powerful image placement. Play up the "Walk Bold" aspect of the title. Perhaps even contrasting someone who's thinking "Hard." Here are a few examples of intriguing covers (though not necessarily related to the genre) I like mainly for aesthetics and creativity. https://www.shopvale.com/dp/Q71MRT2KWD/ https://www.shopvale.com/dp/Q34PLN8XEA
• https://www.shopvale.com/dp/Q925GHV3TC/
• https://www.shopvale.com/dp/Q48DJW6RZB/
• (the font is a little poor in the last one but the image is evoking)
Should not have
• Ugly, tacky, or hard to read fonts. A simple photo with text on top. A simple background with words. Confusing images. Designs with no additional stock image purchase requirements will be given preference over those that do. I've seen a lot of balloons and light bulbs. I'm not saying you can't include them in the design, but if you want to stand out, try to find something more creative that expresses the concept of the title.

```html
<!DOCTYPE html>
<html lang="en">
<head>
<meta charset="utf-8">
<title>Walk Bold Stay Kind — Book Cover</title>
<link href="https://fonts.googleapis.com/css2?family=Poppins:wght@600;700&family=Playfair+Display:ital@1&display=swap" rel="stylesheet">
<style>
  :root {
    --backdrop: #e8e8e8;
    --cover: #1c1c1c;
    --title-yellow: #fff200;
    --accent-red: #c8141c;
    --text-white: #ffffff;
  }
  * { margin: 0; padding: 0; box-sizing: border-box; }
  html, body {
    width: 1114px;
    height: 1200px;
    overflow: hidden;
    background: var(--backdrop);
  }
  .book-cover {
    position: absolute;
    left: 157px;
    top: 39px;
    width: 800px;
    height: 1122px;
    background: var(--cover);
    font-family: "Poppins", sans-serif;
  }
  .title-main {
    position: absolute;
    left: 112px;
    top: 100px;
    font-size: 84px;
    font-weight: 600;
    line-height: 1;
    color: var(--title-yellow);
    letter-spacing: -1px;
    white-space: nowrap;
  }
  .title-sub {
    position: absolute;
    left: 112px;
    top: 180px;
    height: 78px;
    white-space: nowrap;
  }
  .title-sub__lead {
    position: absolute;
    left: 0;
    top: 12px;
    font-family: "Playfair Display", serif;
    font-style: italic;
    font-size: 26px;
    color: var(--text-white);
    line-height: 1;
  }
  .title-sub__word {
    position: absolute;
    left: 52px;
    top: 0;
    font-size: 76px;
    font-weight: 700;
    line-height: 1;
    color: var(--accent-red);
    letter-spacing: -1px;
  }
  .cover-art {
    position: absolute;
    left: 181px;
    top: 316px;
    width: 428px;
    height: 502px;
  }
  .cover-art svg { display: block; width: 100%; height: 100%; }
  .tagline {
    position: absolute;
    left: 88px;
    top: 910px;
    display: flex;
    align-items: center;
    gap: 10px;
  }
  .tagline__number {
    font-size: 108px;
    font-weight: 700;
    color: var(--title-yellow);
    line-height: 1;
    letter-spacing: -3px;
  }
  .tagline__text {
    font-size: 35px;
    font-weight: 600;
    color: var(--text-white);
    line-height: 1.25;
    white-space: nowrap;
  }
</style>
</head>
<body>
  <main class="book-cover">
    <h1 class="title-main">WALK BOLD</h1>
    <div class="title-sub">
      <span class="title-sub__lead">stay</span>
      <span class="title-sub__word">KIND</span>
    </div>

    <div class="cover-art">
      <svg viewBox="0 0 428 502" role="img" aria-label="Illustration of a brain seen from above, left half made of rainbow-coloured particles, right half of white particle network">
        <defs>
          <linearGradient id="spectrum" x1="0" y1="0" x2="0" y2="1">
            <stop offset="0" stop-color="#e8334a"/>
            <stop offset="0.3" stop-color="#e38a2a"/>
            <stop offset="0.5" stop-color="#d7d42e"/>
            <stop offset="0.68" stop-color="#2ab3c8"/>
            <stop offset="0.85" stop-color="#2a63c8"/>
            <stop offset="1" stop-color="#7a2ac8"/>
          </linearGradient>
          <linearGradient id="network" x1="0" y1="0" x2="1" y2="1">
            <stop offset="0" stop-color="#d9d9d9"/>
            <stop offset="1" stop-color="#8a8a8a"/>
          </linearGradient>
          <clipPath id="brain-shape">
            <ellipse cx="214" cy="251" rx="208" ry="247"/>
          </clipPath>
        </defs>
        <g clip-path="url(#brain-shape)">
          <rect x="0" y="0" width="214" height="502" fill="url(#spectrum)"/>
          <rect x="214" y="0" width="214" height="502" fill="url(#network)"/>
        </g>
      </svg>
    </div>

    <div class="tagline">
      <span class="tagline__number">47</span>
      <p class="tagline__text">QUIET RULES FOR<br>CALM AND WONDER</p>
    </div>
  </main>
</body>
</html>
```